" Estamos criando uma empresa dedicada ao comercio varejista, atacadista, a importaçao e exportaçao de doces, balas, chocolates, chicletes, e outros alimentos. "

```html
<!DOCTYPE html>
<html lang="pt-BR">
<head>
<meta charset="UTF-8">
<title>Doce Norte — Cartão de visita</title>
<link rel="stylesheet" href="https://fonts.googleapis.com/css2?family=Montserrat:wght@400;500;700;800&display=swap">
<style>
  :root {
    --navy: #3c4968;
    --navy-deep: #2f3a55;
    --gold: #b8a27a;
    --gold-soft: #c9b692;
    --paper: #f7f7f5;
    --ink: #45506b;
    --muted: #8a92a6;
    --backdrop: #e9e6e1;
  }
  * { box-sizing: border-box; margin: 0; padding: 0; }
  html, body { width: 1200px; height: 1200px; overflow: hidden; }
  body {
    background: var(--backdrop);
    font-family: "Montserrat", sans-serif;
    display: flex;
    flex-direction: column;
    align-items: center;
    justify-content: center;
    gap: 64px;
  }
  .card {
    width: 880px;
    height: 503px;
    position: relative;
    overflow: hidden;
    box-shadow: 0 10px 30px rgba(0,0,0,0.12);
  }

  /* Front */
  .card-front { background: var(--navy); }
  .front-mark-area {
    position: absolute;
    left: 40px; top: 0;
    width: 330px; height: 460px;
    background: linear-gradient(160deg, rgba(201,182,146,0.35), rgba(184,162,122,0.15));
  }
  .front-rule {
    position: absolute;
    left: 0; right: 0; bottom: 26px;
    height: 6px;
    background: var(--paper);
  }
  .front-brand {
    position: absolute;
    left: 470px; top: 205px;
    display: flex;
    align-items: center;
    gap: 18px;
  }
  .brand-dot {
    width: 26px; height: 26px;
    border-radius: 50%;
    background: var(--gold);
  }
  .brand-name {
    font-weight: 800;
    font-size: 52px;
    letter-spacing: 2px;
    line-height: 1;
    text-transform: uppercase;
    color: #ffffff;
  }

  /* Back */
  .card-back { background: var(--paper); }
  .back-top-band {
    position: absolute; left: 0; right: 0; top: 0;
    height: 14px; background: var(--navy);
  }
  .back-bottom-band {
    position: absolute; left: 0; right: 0; bottom: 0;
    height: 70px; background: var(--navy);
    display: flex; align-items: center; justify-content: center; gap: 14px;
    color: #ffffff;
    font-size: 17px; font-weight: 500; letter-spacing: 2px;
    text-transform: uppercase;
  }
  .holder {
    position: absolute; left: 300px; top: 62px;
    display: flex; align-items: flex-start; gap: 16px;
  }
  .holder-name {
    font-size: 30px; font-weight: 500; letter-spacing: 4px;
    text-transform: uppercase; color: var(--ink);
  }
  .holder-role {
    margin-top: 6px;
    font-size: 13px; letter-spacing: 3px;
    text-transform: uppercase; color: var(--muted);
  }
  .contacts {
    position: absolute; left: 60px; top: 175px;
    list-style: none;
    display: flex; flex-direction: column; gap: 22px;
  }
  .contact {
    display: flex; align-items: center; gap: 18px;
    font-size: 15px; letter-spacing: 1.5px;
    text-transform: uppercase; color: var(--ink);
  }
  .contact-lines { display: flex; flex-direction: column; gap: 4px; }
  .icon { width: 22px; height: 22px; flex: none; }
  .back-brand {
    position: absolute; right: 60px; top: 205px;
    display: flex; align-items: center; gap: 14px;
  }
  .back-brand .brand-name { font-size: 38px; color: var(--navy); }
  .back-brand .brand-dot { width: 20px; height: 20px; }
</style>
</head>
<body>

  <section class="card card-front" aria-label="Frente do cartão">
    <div class="front-mark-area" role="img" aria-label="Área do símbolo da marca Doce Norte"></div>
    <div class="front-rule"></div>
    <div class="front-brand">
      <span class="brand-dot"></span>
      <span class="brand-name">Doce Norte</span>
    </div>
  </section>

  <section class="card card-back" aria-label="Verso do cartão">
    <div class="back-top-band"></div>

    <div class="holder">
      <svg class="icon" viewBox="0 0 24 24" fill="var(--ink)" aria-hidden="true">
        <circle cx="12" cy="8" r="4.5"/>
        <path d="M3 22c0-5 4-8 9-8s9 3 9 8z"/>
      </svg>
      <div>
        <p class="holder-name">Tomás Vieira</p>
        <p class="holder-role">Administrador</p>
      </div>
    </div>

    <ul class="contacts">
      <li class="contact">
        <svg class="icon" viewBox="0 0 24 24" fill="none" stroke="var(--ink)" stroke-width="2" aria-hidden="true">
          <rect x="6" y="2" width="12" height="20" rx="2"/>
          <line x1="10" y1="18" x2="14" y2="18"/>
        </svg>
        <div class="contact-lines">
          <span>(11) 2345-6789</span>
          <span>(11) 98765-4321</span>
        </div>
      </li>
      <li class="contact">
        <svg class="icon" viewBox="0 0 24 24" fill="var(--ink)" aria-hidden="true">
          <path d="M12 2a7 7 0 0 0-7 7c0 5 7 13 7 13s7-8 7-13a7 7 0 0 0-7-7zm0 9.5a2.5 2.5 0 1 1 0-5 2.5 2.5 0 0 1 0 5z"/>
        </svg>
        <span>Av. Paulista Nova, 120</span>
      </li>
      <li class="contact">
        <svg class="icon" viewBox="0 0 24 24" fill="none" stroke="var(--ink)" stroke-width="2" aria-hidden="true">
          <rect x="2" y="5" width="20" height="14" rx="1"/>
          <path d="M2 6l10 7 10-7"/>
        </svg>
        <span>tomas@vieira.com</span>
      </li>
    </ul>

    <div class="back-brand">
      <span class="brand-dot"></span>
      <span class="brand-name">Doce Norte</span>
    </div>

    <div class="back-bottom-band">
      <svg class="icon" viewBox="0 0 24 24" fill="none" stroke="#ffffff" stroke-width="1.8" aria-hidden="true">
        <circle cx="12" cy="12" r="10"/>
        <ellipse cx="12" cy="12" rx="4.5" ry="10"/>
        <line x1="2" y1="12" x2="22" y2="12"/>
      </svg>
      <span>www.tomasvieira.com.br</span>
    </div>
  </section>

</body>
</html>
```